Cedar Hall letterhead

We changed our name and logo now need letterhead.
3-4/72 Harlow Street Blacktown 2148
www.cedarhall.org.au
info@cedarhall.org.au
ph: 02 97584120

At this stage, we are preferencing Design #: 5398880 and Design #5401338

```html
<!DOCTYPE html>
<html lang="en">
<head>
<meta charset="utf-8">
<title>Cedar Hall Letterhead</title>
<link href="https://fonts.googleapis.com/css2?family=Raleway:wght@300;400&display=swap" rel="stylesheet">
<style>
  :root {
    --backdrop: #ececec;
    --paper: #fbfbfb;
    --rule-red: #8e1b12;
    --seal-slate: #71838f;
    --ink: #5a5f63;
  }
  html, body {
    margin: 0;
    width: 1200px;
    height: 943px;
    overflow: hidden;
    background: var(--backdrop);
  }
  .letterhead {
    position: absolute;
    left: 289px;
    top: 31px;
    width: 622px;
    height: 880px;
    background: var(--paper);
    box-shadow: 0 2px 10px rgba(0,0,0,0.12);
    font-family: "Raleway", sans-serif;
  }
  .rule-top {
    position: absolute;
    left: 0;
    right: 0;
    top: 76px;
    height: 4px;
    background: var(--rule-red);
  }
  .rule-side {
    position: absolute;
    left: 70px;
    top: 0;
    bottom: 0;
    width: 4px;
    background: var(--rule-red);
  }
  .brand-mark {
    position: absolute;
    left: 34px;
    top: 40px;
    width: 76px;
    height: 76px;
    border-radius: 50%;
    background: var(--seal-slate);
  }
  .brand-name {
    position: absolute;
    left: 120px;
    top: 88px;
    margin: 0;
    font-size: 16px;
    font-weight: 300;
    letter-spacing: 1px;
    color: var(--ink);
    text-transform: uppercase;
  }
  .contact {
    position: absolute;
    right: 34px;
    top: 90px;
    margin: 0;
    padding: 0;
    list-style: none;
    font-size: 9.5px;
    font-weight: 400;
    color: var(--ink);
  }
  .contact li {
    display: flex;
    align-items: center;
    gap: 5px;
    height: 14px;
  }
  .contact svg {
    width: 9px;
    height: 9px;
    flex: none;
  }
</style>
</head>
<body>
  <main class="letterhead">
    <div class="rule-top"></div>
    <div class="rule-side"></div>
    <div class="brand-mark"></div>
    <p class="brand-name">Cedar Hall</p>
    <ul class="contact">
      <li>
        <svg viewBox="0 0 10 10"><circle cx="5" cy="5" r="5" fill="#5a5f63"/><path d="M5 2.2a1.8 1.8 0 0 1 1.8 1.8C6.8 5.4 5 7.8 5 7.8S3.2 5.4 3.2 4A1.8 1.8 0 0 1 5 2.2z" fill="#fff"/></svg>
        3-4/72 Harlow Street Blacktown 2148
      </li>
      <li>
        <svg viewBox="0 0 10 10"><circle cx="5" cy="5" r="5" fill="#5a5f63"/><path d="M3.3 2.6l1 1-.5.8a3.5 3.5 0 0 0 1.8 1.8l.8-.5 1 1-.6.8C5 7.3 2.7 5 2.5 3.2z" fill="#fff"/></svg>
        02 97584120
      </li>
      <li>
        <svg viewBox="0 0 10 10"><circle cx="5" cy="5" r="5" fill="#5a5f63"/><rect x="2.5" y="3.3" width="5" height="3.4" fill="none" stroke="#fff" stroke-width=".7"/><path d="M2.5 3.3L5 5.3l2.5-2" fill="none" stroke="#fff" stroke-width=".7"/></svg>
        info@cedarhall.org.au
      </li>
      <li>
        <svg viewBox="0 0 10 10"><circle cx="5" cy="5" r="5" fill="#5a5f63"/><circle cx="5" cy="5" r="2.6" fill="none" stroke="#fff" stroke-width=".6"/><path d="M2.4 5h5.2M5 2.4c-1.2 1.5-1.2 3.7 0 5.2M5 2.4c1.2 1.5 1.2 3.7 0 5.2" fill="none" stroke="#fff" stroke-width=".5"/></svg>
        www.cedarhall.org.au
      </li>
    </ul>
  </main>
</body>
</html>
```